CD cover for rock-nproll song

I need a logo design for a CD cover for a soon-to-be released rock song by my band, VEXO.
The song is called "Darlin Don't Stay". The logo should include the band logo as well as some representation of the song title. The song is about the end of a romantic relationship.

on -line music consumers

Baby

• VEXO logo (provided)
• Name of song- "Darlin Don't Stay"
• A design that reflects the meaning in the song... "Darlin Don't Stay, it's time to go, it's all over. What you said to me, made me see we've got nothing". That is the chorus- the song is about a relationship coming apart.

```html
<!DOCTYPE html>
<html lang="en">
<head>
<meta charset="utf-8">
<title>Darlin Don't Stay – VEXO</title>
<link rel="stylesheet" href="https://fonts.googleapis.com/css2?family=Didact+Gothic&family=Great+Vibes&display=swap">
<style>
  :root {
    --paper: #ffffff;
    --frame-line: #1a1a1a;
    --sky-top: #8a7038;
    --sky-mid: #b9a35a;
    --sky-glow: #d6d08a;
    --hills: #7a5a2e;
    --bench: #4a2a17;
    --bench-deep: #1f0f08;
    --ink-light: #ffffff;
    --accent-red: #d8351c;
  }
  * { margin: 0; padding: 0; box-sizing: border-box; }
  html, body {
    width: 1200px;
    height: 1200px;
    overflow: hidden;
    background: var(--paper);
  }
  .canvas {
    position: relative;
    width: 1200px;
    height: 1200px;
    background: var(--paper);
    border: 1.5px solid var(--frame-line);
  }
  .cover {
    position: absolute;
    left: 110px;
    top: 110px;
    width: 980px;
    height: 980px;
    overflow: hidden;
  }
  .cover-photo {
    position: absolute;
    inset: 0;
    background: linear-gradient(to bottom,
      var(--sky-top) 0%,
      var(--sky-mid) 25%,
      var(--sky-glow) 46%,
      var(--hills) 58%,
      #6a4424 61%,
      var(--bench) 64%,
      #3a1f10 80%,
      var(--bench-deep) 100%);
  }
  .band-name {
    position: absolute;
    top: 76px;
    left: 0;
    width: 100%;
    text-align: center;
    font-family: "Didact Gothic", "Century Gothic", sans-serif;
    font-size: 41px;
    letter-spacing: 1px;
    color: var(--ink-light);
  }
  .song-title {
    position: absolute;
    top: 672px;
    left: 0;
    width: 100%;
    text-align: center;
    font-family: "Great Vibes", cursive;
    font-size: 112px;
    line-height: 1;
    color: var(--ink-light);
  }
  .song-title .title-accent {
    color: var(--accent-red);
    font-size: 76px;
  }
  .chorus-line {
    position: absolute;
    top: 824px;
    left: 0;
    width: 100%;
    text-align: center;
    font-family: "Didact Gothic", "Century Gothic", sans-serif;
    font-size: 18px;
    line-height: 24px;
    color: var(--accent-red);
  }
</style>
</head>
<body>
  <div class="canvas">
    <section class="cover">
      <div class="cover-photo" role="img" aria-label="Sepia photograph of a couple seen from behind, sitting apart on a wooden bench, looking out at hazy hills under a golden sky"></div>
      <div class="band-name">VEXO LOGO</div>
      <h1 class="song-title">Darlin <span class="title-accent">Don't</span> Stay</h1>
      <p class="chorus-line">It’s time to go, it’s all over. What you said to me,<br>made me see we’ve got nothing”</p>
    </section>
  </div>
</body>
</html>
```